依頼詳細
入れて貰いたいワードです。

焼餃子の画像は用意お願いします。

・餃子の街 宇都宮
・栃木県宇都宮市出身のオーナーの一押し
・白峰の冷凍生餃子
・特製みそだれで旨い
・宇都宮の餃子として28年 多くの方に愛され栃木県内のラーメン店や飲食店でも多く利用されています

【商品】

・白峰の冷凍生餃子 20個入り 680円
・お徳用 白峰の冷凍生餃子 50個入り 1580円

*上記2品、餃子のたれ&特製味噌だれ付

記載項目
【販売店舗】
サニーステップキックボクシング&ジム
北九州市小倉北区旭町2丁目5-3-2F
093-514-2086
営業時間 10~13時 17~20時
*営業時間外に購入ご希望の方は営業時間内にお電話下さいませ。
サイズ
A4
ページ数
片面
希望イメージ
シンプル 複雑
単色 カラフル
暗い 明るい
日常 高級
遊び心 厳粛
未来的 伝統的
女性的 男性的
希望する色
赤系、黄・オレンジ系
納品ファイル
• 高解像度JPG (.jpg)
• イラストレーター形式 (.ai)
依頼詳細

・特製みそだれで旨い ⇒ 包み名人 味噌だれで旨い

に変更お願いします
*画像も添付します

```html
<!DOCTYPE html>
<html lang="ja">
<head>
<meta charset="UTF-8">
<title>白峰の冷凍生餃子</title>
<link rel="stylesheet" href="https://fonts.googleapis.com/css2?family=Dela+Gothic+One&family=Yuji+Syuku&family=Zen+Kaku+Gothic+New:wght@500;700;900&display=swap">
<style>
:root{
  --red:#d8201a;
  --deep-red:#b3120e;
  --yellow:#ffe34a;
  --orange:#f6a321;
  --green:#3f9b2e;
  --black:#161210;
  --white:#ffffff;
  --ink:#2a1a12;
  --photo-light:#e9c489;
  --photo-dark:#9a5a22;
}
*{margin:0;padding:0;box-sizing:border-box}
html,body{width:846px;height:1200px;overflow:hidden;background:var(--white)}
.poster{position:relative;width:846px;height:1200px;overflow:hidden;
  font-family:"Zen Kaku Gothic New",sans-serif;color:var(--ink);
  background:linear-gradient(180deg,var(--yellow) 0,var(--orange) 170px,var(--orange) 100%)}
.gyoza-photo{position:absolute;left:0;top:150px;width:846px;height:860px;
  background:radial-gradient(ellipse at 35% 40%,var(--photo-light),#c98a45 55%,var(--photo-dark) 100%)}
.header-band{position:absolute;left:0;top:0;width:430px;height:160px;background:var(--red);
  clip-path:polygon(0 0,100% 0,88% 100%,0 100%)}
.city-title{position:absolute;left:28px;top:14px;font-family:"Dela Gothic One",sans-serif;
  color:var(--yellow);font-size:50px;line-height:64px;font-weight:400}
.city-title span{display:block;padding-left:74px}
.brand{position:absolute;left:450px;top:8px;text-align:center;width:380px;font-weight:400}
.brand ruby{font-family:"Dela Gothic One",sans-serif;font-size:86px;color:var(--red);
  -webkit-text-stroke:3px var(--black);paint-order:stroke fill}
.brand rt{font-size:20px;color:var(--ink);-webkit-text-stroke:0;letter-spacing:6px}
.brand .no{font-family:"Dela Gothic One",sans-serif;font-size:66px;color:var(--red);
  -webkit-text-stroke:3px var(--black);paint-order:stroke fill}
.tagline{position:absolute;left:58px;top:178px;width:520px;height:150px;transform:rotate(-9deg);
  background:var(--green);border:4px solid var(--white);box-shadow:0 4px 8px rgba(0,0,0,.35);
  font-family:"Dela Gothic One",sans-serif;color:var(--white);padding:10px 24px;font-size:46px;line-height:62px}
.tagline .accent{color:var(--yellow)}
.tagline .line2{display:block;padding-left:110px}
.vertical-title{position:absolute;left:608px;top:165px;width:212px;height:770px;background:var(--black);
  writing-mode:vertical-rl;font-family:"Yuji Syuku",serif;color:var(--white);font-size:146px;
  line-height:212px;text-align:center;letter-spacing:2px}
.package{position:absolute;left:200px;top:362px;width:110px;height:128px;transform:rotate(-8deg);
  background:linear-gradient(160deg,#e07a3a,#a9421c);border:3px solid var(--white)}
.package-large{position:absolute;left:430px;top:914px;width:150px;height:70px;transform:rotate(-4deg);
  background:linear-gradient(160deg,#f4efe6,#d6c9b4);border:3px solid var(--white)}
.story{position:absolute;left:110px;top:500px;width:470px;padding:20px 26px;
  background:rgba(255,255,255,.85);font-size:25px;line-height:36px;font-weight:700}
.products{position:absolute;left:28px;top:700px;width:560px;font-weight:900}
.product{margin-bottom:12px;background:rgba(255,255,255,.8);padding:6px 16px}
.product .name{font-size:32px;line-height:42px;display:block}
.product .name::before{content:"◆";margin-right:4px}
.product .price{font-size:32px;line-height:46px;display:block;padding-left:140px}
.product .price b{font-size:42px;color:var(--deep-red)}
.store{position:absolute;left:0;top:990px;width:846px;height:210px;
  background:linear-gradient(180deg,rgba(255,255,255,.85),var(--white) 35%);padding:14px 40px}
.store-label{font-size:19px;font-weight:900;line-height:28px}
.store-name,.store-address{font-size:19px;font-weight:700;line-height:28px}
.hours{display:flex;gap:30px;align-items:baseline;margin-top:12px}
.hours-main{font-size:21px;font-weight:900;background:var(--yellow);padding:2px 10px}
.hours-note{font-size:14px;font-weight:500}
.phone{position:absolute;left:250px;top:148px;font-family:"Dela Gothic One",sans-serif;
  color:var(--red);font-size:46px;line-height:56px;display:flex;align-items:baseline;gap:10px}
.phone small{font-size:26px}
</style>
</head>
<body>
<div class="poster">
  <div class="gyoza-photo" role="img" aria-label="焼き餃子の写真"></div>
  <div class="header-band"></div>
  <h2 class="city-title">餃子の街<span>宇都宮</span></h2>
  <h1 class="brand"><ruby>白峰<rt>しらみね</rt></ruby><span class="no">の</span></h1>
  <p class="tagline"><span class="accent">包み名人</span><span class="line2">味噌だれで旨い!!</span></p>
  <div class="vertical-title">冷凍生餃子</div>
  <div class="package" role="img" aria-label="冷凍生餃子20個入りのパッケージ写真"></div>
  <p class="story">宇都宮の餃子として28年<br>多くの方に愛され栃木県内の<br>ラーメン店や飲食店でも<br>多く利用されています</p>
  <div class="products">
    <div class="product"><span class="name">白峰の冷凍生餃子</span><span class="price">20個入り <b>680</b>円</span></div>
    <div class="product"><span class="name">お徳用 白峰の冷凍生餃子</span><span class="price">50個入り <b>1580</b>円</span></div>
  </div>
  <div class="package-large" role="img" aria-label="冷凍生餃子50個入りのパッケージ写真"></div>
  <section class="store">
    <p class="store-label">【販売店舗】</p>
    <p class="store-name">サニーステップキックボクシング&amp;ジム</p>
    <p class="store-address">北九州市小倉北区旭町2丁目5-3-2F</p>
    <div class="hours"><span class="hours-main">営業時間/10~13時　17~20時</span>
      <span class="hours-note">*営業時間外に購入ご希望の方は営業時間内にお電話下さいませ。</span></div>
    <p class="phone"><small>Tel.</small>093-514-2086</p>
  </section>
</div>
</body>
</html>
```